Startup company business card (Media & Advertising)

we need a business card design for a company that is a startup in the media and aggregation industry. Card needs to look funky and of a new breed/modern and upmarket.

Target Market(s)

advertisers/ brand agencies & media publishers

Industry/Entity Type

Advertising

Contact Information for Business Card

Please ensure the front face signifies our brand (plumvexo.com) and back has details for the contact. Standard contact such as phone , address, email , website etc.

Font styles to use
Other font styles liked:
• use styleguide and logo font and color

Colors

Designer to choose colors to be used in the design.

Requirements
Must have
• We are disrupting the media and agency industry so subtlety would be good to use imagery to signify this
Nice to have
• Please use logo colors for branding
Should not have
• be as creative and provide few options. Pick a brand color from logo and styleguide

```html
<!DOCTYPE html>
<html lang="en">
<head>
<meta charset="utf-8">
<title>Plumvexo Business Card</title>
<link href="https://fonts.googleapis.com/css2?family=Arvo:wght@700&family=Open+Sans:wght@400;700&display=swap" rel="stylesheet">
<style>
  :root {
    --page-bg: #ece8e4;
    --card-plum: #561e2d;
    --brand-red: #e8394a;
    --ink-light: #ffffff;
  }
  * { margin: 0; padding: 0; box-sizing: border-box; }
  html, body { width: 1200px; height: 1000px; overflow: hidden; }
  body {
    background: var(--page-bg);
    position: relative;
    font-family: "Open Sans", Arial, sans-serif;
  }
  .card {
    position: absolute;
    left: 234px;
    width: 734px;
    height: 419px;
    background: var(--card-plum);
    border-radius: 16px;
    box-shadow: 0 6px 14px rgba(0,0,0,0.25);
  }
  .card--front { top: 57px; }
  .card--back { top: 524px; }

  .brand-mark {
    position: absolute;
    border-radius: 50%;
    background: var(--brand-red);
  }
  .card--front .brand-mark { left: 130px; top: 170px; width: 90px; height: 90px; }
  .card--back .brand-mark { left: 90px; top: 116px; width: 190px; height: 190px; }

  .brand-name {
    position: absolute;
    left: 290px;
    top: 172px;
    font-family: "Arvo", Georgia, serif;
    font-weight: 700;
    font-size: 64px;
    line-height: 80px;
    color: var(--ink-light);
  }

  .website {
    position: absolute;
    left: 0; right: 0;
    bottom: 22px;
    text-align: center;
    font-weight: 700;
    font-size: 22px;
    color: var(--brand-red);
  }

  .contact-list {
    position: absolute;
    left: 420px;
    top: 150px;
    list-style: none;
    color: var(--ink-light);
    font-size: 16px;
    line-height: 21px;
  }
  .contact-item {
    display: flex;
    align-items: flex-start;
    margin-bottom: 18px;
  }
  .contact-icon {
    width: 22px;
    height: 21px;
    margin-right: 15px;
    flex-shrink: 0;
    fill: var(--ink-light);
  }
</style>
</head>
<body>
  <section class="card card--front" aria-label="Card front">
    <div class="brand-mark" aria-hidden="true"></div>
    <h1 class="brand-name">Plumvexo</h1>
    <p class="website">plumvexo.com</p>
  </section>

  <section class="card card--back" aria-label="Card back">
    <div class="brand-mark" aria-hidden="true"></div>
    <ul class="contact-list">
      <li class="contact-item">
        <svg class="contact-icon" viewBox="0 0 24 24" aria-hidden="true"><path d="M6.6 10.8a15.2 15.2 0 0 0 6.6 6.6l2.2-2.2c.3-.3.7-.4 1-.2 1.1.4 2.3.6 3.6.6.6 0 1 .4 1 1V20c0 .6-.4 1-1 1C10.6 21 3 13.4 3 4c0-.6.4-1 1-1h3.5c.6 0 1 .4 1 1 0 1.3.2 2.5.6 3.6.1.3 0 .7-.2 1z"/></svg>
        <span>+109876543210</span>
      </li>
      <li class="contact-item">
        <svg class="contact-icon" viewBox="0 0 24 24" aria-hidden="true"><path d="M2 5h20v14H2z M3.5 6.5 12 13l8.5-6.5" fill="none" stroke="#fff" stroke-width="1.8"/><path d="M2 5h20L12 12.5z"/></svg>
        <span>hello@plumvexo.com</span>
      </li>
      <li class="contact-item">
        <svg class="contact-icon" viewBox="0 0 24 24" aria-hidden="true"><path d="M12 2a7 7 0 0 0-7 7c0 5.2 7 13 7 13s7-7.8 7-13a7 7 0 0 0-7-7zm0 9.5A2.5 2.5 0 1 1 12 6.5a2.5 2.5 0 0 1 0 5z"/></svg>
        <span>58 Larkmoor Lane, Fenwick Row,<br>Oregon</span>
      </li>
    </ul>
    <p class="website">plumvexo.com</p>
  </section>
</body>
</html>
```